Webdesign für die Veranstaltungsreihe Wolkenreigen
Zielgruppe
Für die Veranstaltungsreihe 'Wolkenreigen' soll ein Website-Design entwickelt werden, welches potentielle Besucher über die Veranstaltung informiert (Standorte, Anfahrt, Preise etc.) und gleichzeitig eine Foto- bzw. Videodokumentation der vergangenen 'Wolkenreigen' bietet.
Zielgruppe:
Personen jeder Altersgruppe, Gruppen wie (Familien, Vereine etc.)
Aufgabenstellung
Das Design sollte...
einfach und modern
nicht zu verspielt
freundlich
kreativ
innovativ
den Inhalt der Veranstaltungsreihe
...wiederspiegeln.
Bitte orientieren Sie sich an dem bestehenden Design der Eventreihe.

```html
<!DOCTYPE html>
<html lang="de">
<head>
<meta charset="utf-8">
<title>Wolkenreigen – Tickets &amp; Preise</title>
<link href="https://fonts.googleapis.com/css2?family=Ubuntu:ital,wght@0,300;0,400;0,500;0,700;1,400;1,500;1,700&family=Fira+Sans:wght@300;700&display=swap" rel="stylesheet">
<style>
:root{
  --night:#151515;
  --gold:#f7b230;
  --gold-light:#fdd77e;
  --gold-pale:#fde7a8;
  --ink:#222;
  --muted:#555;
  --white:#fff;
  --card-line:#e6e6e6;
}
*{box-sizing:border-box;margin:0;padding:0}
html,body{width:1058px;height:1200px;overflow:hidden}
body{font-family:"Ubuntu",sans-serif;color:var(--ink);background:var(--white);position:relative}

.site-header{position:absolute;left:0;top:0;width:1058px;height:127px;
  background:radial-gradient(ellipse at 20% 60%,#3a2a12 0%,transparent 45%),radial-gradient(ellipse at 80% 40%,#3a2a12 0%,transparent 45%),var(--night)}
.header-item{position:absolute;top:45px;display:flex;align-items:center;gap:10px;color:var(--white);font-size:8.5px;line-height:10px}
.header-item b{font-weight:700}
.header-icon{width:18px;height:26px;flex:none}
.brand{position:absolute;left:384px;top:28px;width:290px;text-align:center;color:var(--white)}
.brand-name{font-size:40px;font-weight:700;color:var(--gold);letter-spacing:-0.5px;line-height:42px}
.brand-claim{font-size:14px;font-weight:700;letter-spacing:0.3px;margin-top:2px}
.brand-sub{display:flex;align-items:center;justify-content:center;gap:8px;color:var(--gold);font-size:9.5px;font-weight:700;margin-top:1px}
.brand-sub::before,.brand-sub::after{content:"";width:24px;height:1.5px;background:var(--gold)}

.main-nav{position:absolute;left:0;top:127px;width:1058px;height:38px;
  background:linear-gradient(#fde39a 0%,#fcd172 45%,#f7b535 100%);display:flex;padding-left:207px}
.main-nav a{display:flex;align-items:center;justify-content:center;height:38px;color:var(--white);text-decoration:none;font-size:10.5px;
  border-left:1px solid rgba(200,140,30,.5);text-shadow:0 1px 1px rgba(150,90,0,.35)}
.main-nav a:last-child{border-right:1px solid rgba(200,140,30,.5)}

.hero{position:absolute;left:0;top:165px;width:1058px;height:221px;
  background:radial-gradient(ellipse at 15% 80%,#8a4a12 0%,transparent 40%),radial-gradient(ellipse at 85% 70%,#8a4a12 0%,transparent 40%),radial-gradient(ellipse at 50% 30%,#5a3410 0%,transparent 55%),#0d0a06;
  text-align:center;color:var(--white)}
.hero h1{font-family:"Fira Sans",sans-serif;font-weight:700;font-size:39px;margin-top:44px;line-height:44px}
.hero p{font-family:"Fira Sans",sans-serif;font-weight:300;font-size:30px;line-height:34px;letter-spacing:1px}
.hero-button{display:inline-block;margin-top:14px;background:linear-gradient(#fcd37a,#f7b230);color:var(--white);font-weight:700;font-size:11.5px;padding:9px 18px;text-decoration:none}

.buy-options{position:absolute;top:418px;left:0;width:1058px}
.buy-option{position:absolute;display:flex;gap:22px}
.buy-icon{width:44px;height:44px;background:var(--gold);display:flex;align-items:center;justify-content:center;flex:none}
.buy-option h2{color:var(--gold);font-style:italic;font-weight:700;font-size:12.5px;margin-top:7px}
.buy-option p{font-size:8.3px;line-height:10.5px}

.events{position:absolute;left:0;top:496px;width:1058px;height:454px;
  background:radial-gradient(ellipse at 20% 40%,#efe0c9 0%,transparent 50%),radial-gradient(ellipse at 80% 60%,#efe0c9 0%,transparent 50%),#ece8e4}
.event-card{position:absolute;top:50px;width:165px;height:352px;background:var(--white);display:flex;flex-direction:column}
.event-photo{height:97px;position:relative}
.event-date{position:absolute;right:5px;top:4px;color:var(--white);font-style:italic;font-weight:500;font-size:9.5px}
.event-body{padding:9px 11px 0;font-size:7.3px;line-height:14.3px}
.event-body h3{color:var(--gold);font-weight:400;font-size:16px;line-height:20px;margin-bottom:12px}
.event-body h4{color:var(--gold);font-weight:500;font-size:8.3px;line-height:11px}
.price-row{display:grid;grid-template-columns:99px 1fr}
.price-row b{font-style:italic;font-weight:700}
.event-note{font-size:6px;line-height:14.3px}
.event-note.small{line-height:8px;font-style:italic;margin-top:6px}
.event-divider{height:1px;background:var(--card-line);margin:7px -6px 10px}
.event-button{margin-top:auto;height:27px;background:linear-gradient(#fcd67f,#f7b230);color:var(--white);font-size:10.5px;display:flex;align-items:center;justify-content:center;text-decoration:none}

.general-info{position:absolute;left:178px;top:970px;width:700px;font-size:7px;line-height:9.5px}
.general-info h2{font-weight:300;font-size:16px;margin-bottom:24px}
.general-info h2 span{color:var(--gold);font-weight:700}
.general-info em{color:var(--gold);font-weight:500;display:block}
.general-info p{margin-bottom:18px}

.site-footer{position:absolute;left:0;top:1154px;width:1058px;height:46px;background:var(--night);color:var(--white);font-size:6px;font-weight:700}
.footer-social{position:absolute;left:208px;top:18px;display:flex;gap:16px}
.footer-social span{width:9px;height:9px;border-radius:50%;background:var(--white)}
.footer-copy{position:absolute;left:465px;top:20px}
.footer-links{position:absolute;left:733px;top:20px;font-weight:400}
</style>
</head>
<body>

<header class="site-header" role="img" aria-label="Dunkler Hintergrund mit Feuerwerk">
  <div class="header-item" style="left:94px">
    <svg class="header-icon" viewBox="0 0 18 26"><rect x="2" y="6" width="14" height="14" fill="var(--gold)"/></svg>
    <div>Follow us on<br><b>socialnetz.de/</b><br><b>Wolkenreigen</b></div>
  </div>
  <div class="header-item" style="left:227px">
    <svg class="header-icon" viewBox="0 0 24 26" style="width:26px"><path d="M2 8l18-4 2 5-18 4z M2 13l18-4 2 5-18 4z M2 18l18-4 2 5-18 4z" fill="var(--gold)"/></svg>
    <div>Verfügbare Tickets<br>finden Sie im<br><b>kartenwerk.de - Shop</b></div>
  </div>
  <div class="brand">
    <div class="brand-name">WOLKENREIGEN</div>
    <div class="brand-claim">DER WETTSTREIT DER PYROTECHNIKER</div>
    <div class="brand-sub">DREI FANTASTISCHE MUSIKFEUERWERKE</div>
  </div>
  <div class="header-item" style="left:716px">
    <svg class="header-icon" viewBox="0 0 18 26"><rect x="2" y="1" width="14" height="24" rx="2" fill="none" stroke="var(--gold)" stroke-width="2.5"/><rect x="4" y="4" width="10" height="15" fill="var(--gold)"/><circle cx="9" cy="22" r="1.3" fill="var(--gold)"/></svg>
    <div>Unsere Service<br>HOTLINE<br><b>(02 09) 555 01 234</b></div>
  </div>
  <div class="header-item" style="left:864px">
    <svg class="header-icon" viewBox="0 0 26 26" style="width:26px"><circle cx="13" cy="13" r="12" fill="var(--gold)"/></svg>
    <div>Follow us on<br><b>bildnetz.de/</b><br><b>wolkenreigen</b></div>
  </div>
</header>

<nav class="main-nav">
  <a href="#" style="width:118px">Home</a>
  <a href="#" style="width:117px">Standorte</a>
  <a href="#" style="width:140px">Tickets &amp; Preise</a>
  <a href="#" style="width:140px">Fotos &amp; Videos</a>
  <a href="#" style="width:129px">FAQ / Regeln</a>
</nav>

<section class="hero" role="img" aria-label="Goldenes Feuerwerk am Nachthimmel">
  <h1>TICKETS &amp; PREISE</h1>
  <p>ZU ALLEN VERANSTALTUNGEN 2017</p>
  <a class="hero-button" href="#">TICKETS KAUFEN!</a>
</section>

<section class="buy-options">
  <div class="buy-option" style="left:265px">
    <div class="buy-icon"><svg width="26" height="26" viewBox="0 0 26 26"><rect x="7" y="7" width="12" height="12" fill="var(--white)"/></svg></div>
    <div>
      <h2>Tickets bei Kartenwerk kaufen</h2>
      <p>Ticket-Hotline: 01806 / 555 010<br>(0,14 €/Minute Mobil-Tel. max. 0,42 €/Minute)</p>
    </div>
  </div>
  <div class="buy-option" style="left:571px">
    <div class="buy-icon"><svg width="22" height="28" viewBox="0 0 22 28"><path d="M11 27C4 17 1 13 1 10a10 10 0 0 1 20 0c0 3-3 7-10 17z" fill="var(--white)"/><circle cx="11" cy="10" r="4" fill="var(--gold)"/></svg></div>
    <div>
      <h2>Tickets vor Ort kaufen</h2>
      <p>entweder im Vorverkauf <b><i>(zur Übersicht)</i></b><br>oder vor Ort an den Abendkassen</p>
    </div>
  </div>
</section>

<section class="events" role="img" aria-label="Heller, blasser Feuerwerkshintergrund">
  <article class="event-card" style="left:178px">
    <div class="event-photo" role="img" aria-label="Beleuchtetes Schlossgebäude bei Dämmerung" style="background:linear-gradient(#3a5b8c,#6d7fa0 55%,#8c7b52 80%,#2d2a22)"><span class="event-date">18. Juni 2016</span></div>
    <div class="event-body">
      <h3>Braunschweig</h3>
      <h4>Vorverkauf:</h4>
      <div class="price-row"><span>Stehplatz Erwachsene</span><b>10,00 €*</b></div>
      <div class="price-row"><span>Sitzplatz</span><b>20,50 €*</b></div>
      <div class="price-row"><span>Sitzplatz mit Bonus-Paket</span><b>44,95 €*</b></div>
      <p class="event-note small">Das Bonus-Paket beinhaltet: Sitzplatz-Ticket, Open-Air-Poncho, Wolkenreigen-Tragetasche, Soft-Drink 0,3l und Programmheft</p>
      <p class="event-note">*zzgl. Vorverkaufs-Gebühren</p>
      <div class="event-divider"></div>
      <h4>Abendkasse:</h4>
      <div class="price-row"><span>Stehplatz Erwachsene</span><b>16,00 €</b></div>
      <div class="price-row"><span>Sitzplatz</span><b>27,00 €</b></div>
    </div>
    <a class="event-button" href="#">Tickets bei Kartenwerk kaufen</a>
  </article>

  <article class="event-card" style="left:357px">
    <div class="event-photo" role="img" aria-label="Gelb beleuchtetes Schloss bei Nacht" style="background:linear-gradient(#121833,#1d2240 40%,#b08418 60%,#e0b020 80%,#2a2010)"><span class="event-date">18. Juni 2016</span></div>
    <div class="event-body">
      <h3>Paderborn</h3>
      <h4>Vorverkauf:</h4>
      <div class="price-row"><span>Stehplatz Jugendliche</span><b>6,50 €*</b></div>
      <div class="price-row"><span>(12 bis 17 Jahre)</span><b></b></div>
      <div class="price-row"><span>Stehplatz Erwachsene</span><b>9,50 €*</b></div>
      <div class="price-row"><span>Sitzplatz</span><b>19,50 €*</b></div>
      <p class="event-note">*zzgl. Vorverkaufs-Gebühren</p>
      <div class="event-divider"></div>
      <h4>Abendkasse:</h4>
      <div class="price-row"><span>Stehplatz Jugendliche</span><b>9,00 €*</b></div>
      <div class="price-row"><span>(12 bis 17 Jahre)</span><b></b></div>
      <div class="price-row"><span>Stehplatz Erwachsene</span><b>16,00 €*</b></div>
      <div class="price-row"><span>Sitzplatz</span><b>26,00 €*</b></div>
    </div>
    <a class="event-button" href="#">Tickets bei Kartenwerk kaufen</a>
  </article>

  <article class="event-card" style="left:536px">
    <div class="event-photo" role="img" aria-label="Beleuchteter Industrieturm mit Wasserbecken bei Nacht" style="background:linear-gradient(#1a1610,#3a2418 45%,#6a4020 65%,#1a140c)"><span class="event-date">18. Juni 2016</span></div>
    <div class="event-body">
      <h3>Oberhausen</h3>
      <h4>Vorverkauf:</h4>
      <div class="price-row"><span>Stehplatz Erwachsene</span><b>9,50 €*</b></div>
      <div class="price-row"><span>Sitzplatz</span><b>20,50 €*</b></div>
      <p class="event-note">*zzgl. Vorverkaufs-Gebühren<br>Der Ticket-Vorverkauf endet einen Tag vor der Veranstaltung, danach sind die Tickets nur noch an der Abendkasse erhältlich.</p>
      <div class="event-divider"></div>
      <h4>Abendkasse:</h4>
      <div class="price-row"><span>Stehplatz Erwachsene</span><b>16,00 €*</b></div>
      <div class="price-row"><span>Sitzplatz</span><b>27,00 €*</b></div>
      <p class="event-note">Keine EC- oder Kreditkartenzahlung möglich!</p>
    </div>
    <a class="event-button" href="#">Tickets bei Kartenwerk kaufen</a>
  </article>

  <article class="event-card" style="left:714px">
    <div class="event-photo" role="img" aria-label="Beleuchtetes Schloss mit Vorplatz bei Nacht" style="background:linear-gradient(#0c0c10,#1a1510 45%,#c08828 62%,#3a2a14 75%,#0c0c0c)"><span class="event-date">18. Juni 2016</span></div>
    <div class="event-body">
      <h3>Karlsruhe</h3>
      <h4>Vorverkauf:</h4>
      <div class="price-row"><span>Stehplatz Erwachsene</span><b>9,50 €*</b></div>
      <div class="price-row"><span>Sitzplatz</span><b>20,50 €*</b></div>
      <p class="event-note">*zzgl. Vorverkaufs-Gebühren<br>Der Ticket-Vorverkauf endet einen Tag vor der Veranstaltung, danach sind die Tickets nur noch an der Abendkasse erhältlich.</p>
      <div class="event-divider"></div>
      <h4>Abendkasse:</h4>
      <div class="price-row"><span>Stehplatz Erwachsene</span><b>16,00 €*</b></div>
      <div class="price-row"><span>Sitzplatz</span><b>27,00 €*</b></div>
      <p class="event-note">Keine EC- oder Kreditkartenzahlung möglich!</p>
    </div>
    <a class="event-button" href="#">Tickets bei Kartenwerk kaufen</a>
  </article>
</section>

<section class="general-info">
  <h2><span>Allgemeine</span> Informationen:</h2>
  <p><em><i>Kinder unter 12 Jahren haben im Stehplatzbereich freien Eintritt!</i></em>Bei mobilitätseingeschränkten Personen mit Behindertenausweis-Kennzeichnung "B" oder höher bekommt eine Begleitperson kostenfreien Eintritt.</p>
  <p style="margin-bottom:10px">Tickets für die Veranstaltung sind neben den nebenstehenden Vorverkaufsstellen auch in allen bekannten (Konzert-)Ticketvorverkaufstellen erhältlich.</p>
  <p><em><i>Wichtiger Hinweis:</i></em>Auf Karten, die bei lokalen Vorverkaufsstellen ohne Anbindung an das Kartenwerk- oder TixPunkt-System gekauft werden, können mitunter sehr hohe Vorverkaufsgebühren aufgeschlagen sein. Wir empfehlen daher dringend, die Tickets entweder online oder an einer der hier aufgelisteten Vorverkaufsstellen zu erwerben.</p>
  <p>Mit dem Kauf von Tickets akzeptieren Sie die Allgemeinen Geschäftsbedingungen, die im Impressum eingesehen werden können.</p>
</section>

<footer class="site-footer">
  <div class="footer-social"><span></span><span></span><span></span><span></span><span></span><span></span></div>
  <div class="footer-copy">COPYRIGHT 2016. ALL RIGHTS RESERVED</div>
  <div class="footer-links">FAQ &nbsp;|&nbsp; AGB &nbsp;|&nbsp; IMPRESSUM &nbsp;|&nbsp; KONTAKT</div>
</footer>

</body>
</html>
```